Charity Initiative needs a WebPage design

We need a web design for charity initiative by two young guys riding their bikes around Australia to support KestrelWay which helps people with depression and anxiety. Full brief and requirements are attached in the PDF and word document. We have the logo already done and attached. Website will be done in Wordpress and need to get Donations, display current donations, show live Video feed, GPS tracker, Blogs etc and also ability to sell merchandise later

Target Market(s)

Sponsors, Business, Young People

Number of Pages Required

4 page

Font styles to use
Serif
Sans Serif
Decorative
Script

Requirements
Must have
• As per Brief and also Donation status etc
Nice to have
• Please check my logo and read the Bried

```html
<!DOCTYPE html>
<html lang="en">
<head>
<meta charset="utf-8">
<title>Throttle North – The Motorcycle Adventure Around Australia</title>
<link rel="stylesheet" href="https://fonts.googleapis.com/css2?family=Bangers&family=Roboto+Condensed:wght@400;700&family=Roboto:wght@400;500;700&family=Lato:wght@400;700&display=swap">
<style>
:root{
  --pink:#e8266f;
  --pink-deep:#c81f5e;
  --teal:#3bb3a5;
  --teal-dark:#2a8f86;
  --black:#0b0b0b;
  --white:#ffffff;
  --ink:#222;
  --grey:#555;
  --stage:#3a3f45;
}
*{box-sizing:border-box;margin:0;padding:0}
html,body{width:1200px;height:2525px;overflow:hidden}
body{background:var(--stage);font-family:"Roboto",Arial,sans-serif;color:var(--ink);position:relative}
.page{position:absolute;left:162px;top:0;width:876px;height:2525px;background:var(--white)}
section,header,nav,footer{position:absolute;left:0;width:876px}

/* header */
.site-header{top:0;height:182px;background:var(--white)}
.brand{position:absolute;left:24px;top:38px;display:flex;align-items:center;gap:14px}
.brand-dot{width:64px;height:64px;border-radius:50%;background:var(--pink)}
.brand-name{font-family:"Bangers",cursive;font-size:58px;color:var(--teal);letter-spacing:1px;line-height:1}
.btn-donate-top{position:absolute;left:651px;top:64px;width:180px;height:54px;background:var(--pink);color:var(--white);font-family:"Bangers",cursive;font-size:30px;letter-spacing:1px;display:flex;align-items:center;justify-content:center;text-decoration:none}

/* nav */
.main-nav{top:182px;height:42px;background:var(--black);display:flex;align-items:center}
.nav-links{display:flex;list-style:none;margin-left:22px}
.nav-links li a{display:block;color:var(--white);text-decoration:none;font-weight:500;font-size:17px;padding:0 18px;line-height:42px}
.nav-links li.active a{background:var(--teal);padding:0 14px;line-height:26px;margin-top:8px}
.social{position:absolute;right:26px;top:8px;display:flex;gap:8px}
.social span{width:27px;height:27px;border:1.5px solid var(--white);display:block}

/* hero */
.hero{top:224px;height:446px;background:var(--pink)}
.hero-video{position:absolute;left:29px;top:37px;width:382px;height:256px;border:4px solid var(--black);background:linear-gradient(160deg,#4c7a3a,#8eb35a 45%,#6d6f70)}
.play{position:absolute;left:50%;top:50%;width:84px;height:84px;margin:-42px 0 0 -42px}
.hero-title{position:absolute;left:438px;top:28px;font-family:"Bangers",cursive;color:var(--white);font-size:36px;line-height:1.05;letter-spacing:1px;font-weight:400}
.stats{position:absolute;left:432px;top:139px;width:417px;height:131px;background:var(--black);display:flex;align-items:center}
.stat{flex:1;text-align:center;color:var(--white)}
.stat+.stat{border-left:1px solid #444}
.stat-label{font-size:22px}
.stat-value{font-family:"Roboto Condensed",sans-serif;font-weight:700;font-size:30px;color:var(--pink);margin-top:12px}
.hero-tagline{position:absolute;left:0;width:100%;top:300px;text-align:center;font-family:"Bangers",cursive;color:var(--white);font-size:34px;letter-spacing:1px;line-height:1}
.hero-sub{position:absolute;left:0;width:100%;top:338px;text-align:center;font-size:29px;color:var(--black);line-height:1.1}
.btn-teal{position:absolute;background:var(--teal);color:var(--white);font-size:21px;display:flex;align-items:center;justify-content:center;text-decoration:none}
.hero .btn-teal{left:359px;top:390px;width:175px;height:41px}

/* section headings */
.section-title{position:absolute;left:0;width:100%;text-align:center;font-family:"Roboto Condensed",sans-serif;font-weight:700;font-size:44px}
.section-title::after{content:"";display:block;width:88px;height:4px;background:var(--black);margin:12px auto 0}
.accent{color:var(--pink)}

/* location */
.location{top:670px;height:456px;background:var(--white)}
.location .section-title{top:20px;color:var(--teal)}
.location .section-title::after{margin-top:10px}
.map{position:absolute;left:0;top:108px;width:876px;height:348px;background:linear-gradient(135deg,#e7e3dc,#efece6 50%,#dedad2)}

/* funds */
.funds{top:1126px;height:444px;overflow:hidden}
.funds-scene{position:absolute;left:0;top:0;width:100%;height:100%;
  background:linear-gradient(180deg,#7fc6c2 0%,#a6dad6 30%,#bfe5e2 50%,#86bdb9 62%,#5c8f8e 72%,#3f9a95 81%,#86b150 84%,#6d9a42 89%,#5b6065 90%,#4a4f54 100%)}
.funds .section-title{top:36px;color:var(--black)}
.tag{position:absolute;background:var(--black);color:var(--pink);font-weight:700;text-align:center;border-radius:4px}
.tag::after{content:"";position:absolute;left:50%;bottom:-9px;margin-left:-9px;border:9px solid transparent;border-bottom:0;border-top-color:var(--black)}
.tag-cap{position:absolute;font-size:13px;font-weight:700;color:var(--black);text-align:center}
.track{position:absolute;left:50px;top:215px;width:776px;height:54px;background:var(--black);display:flex;align-items:center;justify-content:space-around;padding:0 10px}
.track i{display:block;width:22px;height:4px;background:var(--white)}
.rider-marker{position:absolute;left:150px;top:228px;width:28px;height:28px;border-radius:50%;background:var(--pink)}
.btn-pink{position:absolute;left:352px;top:304px;width:175px;height:56px;background:var(--pink);color:var(--white);font-size:22px;display:flex;align-items:center;justify-content:center;text-decoration:none}

/* journals */
.journals{top:1570px;height:423px;background:linear-gradient(180deg,#d42a6a 0%,#c8235f 55%,#e0386f 100%)}
.journals .section-title{top:24px;color:var(--white)}
.journal{position:absolute;top:118px;width:342px}
.journal-img{position:relative;height:125px;border:2px solid #ddd;background:linear-gradient(160deg,#6d7d86,#9aa3a0 50%,#4f5a4e)}
.journal-date{position:absolute;left:0;top:0;background:var(--black);color:var(--white);text-align:center;padding:2px 5px;font-weight:700;line-height:1}
.journal-date b{display:block;font-size:24px}
.journal-date small{display:block;font-size:9px}
.journal-meta{text-align:right;color:var(--white);font-size:11px;margin-top:4px;padding-right:10px}
.journal h3{color:var(--white);font-family:"Lato",sans-serif;font-weight:700;font-size:15px;margin:2px 0 0 4px}
.journal p{color:var(--white);font-family:"Lato",sans-serif;font-size:13.5px;line-height:1.4;margin:4px 0 0 4px}
.btn-black{display:flex;align-items:center;justify-content:center;background:var(--black);color:var(--white);font-family:"Lato",sans-serif;font-weight:700;font-size:13px;text-decoration:none;width:100px;height:30px}
.journal .btn-black{margin:10px 0 0 4px}

/* team */
.team{top:1993px;height:397px;background:var(--white)}
.member{position:absolute;top:62px;width:230px;margin-left:-115px;text-align:center}
.avatar{width:135px;height:135px;border-radius:50%;margin:0 auto;background:linear-gradient(160deg,#8a7a66,#c9b29a)}
.avatar.partner{background:#eeeeee;display:flex;align-items:center;justify-content:center;font-size:15px;color:#3a7fc0;font-weight:500}
.member h3{font-weight:500;font-size:24px;margin-top:20px;color:var(--ink)}
.member p{font-size:12.5px;line-height:1.45;color:var(--grey);margin-top:10px}
.member .btn-black{margin:18px auto 0}

/* newsletter */
.newsletter{top:2390px;height:89px;background:var(--teal);display:flex;align-items:center}
.newsletter label{color:var(--white);font-size:15px;margin-left:65px}
.newsletter .field{margin-left:12px;width:298px;height:33px;border:1px solid var(--white);color:var(--white);font-size:13px;display:flex;align-items:center;padding-left:12px}
.newsletter .subscribe{margin-left:12px;width:104px;height:33px;border:1px solid var(--white);color:var(--white);font-size:13px;font-weight:700;display:flex;align-items:center;justify-content:center}

/* footer */
.site-footer{top:2479px;height:46px;background:var(--black);color:var(--white);display:flex;align-items:center;font-family:"Lato",sans-serif;font-size:13px;font-weight:700}
.site-footer .copy{margin-left:24px}
.payments{margin-left:auto;margin-right:16px;display:flex;align-items:center;gap:6px}
.payments span.card{width:40px;height:26px;background:#f2f2f2;border-radius:3px;display:block}
</style>
</head>
<body>
<div class="page">

  <header class="site-header">
    <div class="brand"><span class="brand-dot"></span><span class="brand-name">Throttle North</span></div>
    <a class="btn-donate-top" href="#donate">Donate Now</a>
  </header>

  <nav class="main-nav">
    <ul class="nav-links">
      <li class="active"><a href="#">Home</a></li>
      <li><a href="#">Journal</a></li>
      <li><a href="#">Riders</a></li>
      <li><a href="#">Riders</a></li>
      <li><a href="#">Contact Us</a></li>
    </ul>
    <div class="social"><span></span><span></span><span></span><span></span><span></span></div>
  </nav>

  <section class="hero">
    <div class="hero-video" role="img" aria-label="Video still of two riders cornering on motorcycles along a forest road">
      <svg class="play" viewBox="0 0 84 84"><circle cx="42" cy="42" r="38" fill="#e8266f" stroke="#fff" stroke-width="4" opacity=".9"/><path d="M34 26 L60 42 L34 58 Z" fill="#fff"/></svg>
    </div>
    <h1 class="hero-title">The Motorcycle Adventure<br>Around Australia</h1>
    <div class="stats">
      <div class="stat"><div class="stat-label">Days</div><div class="stat-value">50</div></div>
      <div class="stat"><div class="stat-label">Kilometers</div><div class="stat-value">10,568</div></div>
      <div class="stat"><div class="stat-label">Provinces</div><div class="stat-value">33</div></div>
    </div>
    <p class="hero-tagline">We Helps People With Depression And Anxiety</p>
    <p class="hero-sub">Donate to our partner charity</p>
    <a class="btn-teal" href="#donate">Donate Now</a>
  </section>

  <section class="location">
    <h2 class="section-title">Current <span class="accent">Location</span></h2>
    <div class="map" role="img" aria-label="Street map showing the riders' live GPS position"></div>
  </section>

  <section class="funds" id="donate">
    <div class="funds-scene" role="img" aria-label="Illustrated landscape of mountains, green verge and an open road under a cloudy sky"></div>
    <h2 class="section-title">Fund <span class="accent">Raised</span></h2>
    <span class="tag-cap" style="left:18px;top:148px;width:70px">We Started</span>
    <div class="tag" style="left:27px;top:168px;width:42px;height:28px;line-height:28px;font-size:13px">00 $</div>
    <span class="tag-cap" style="left:182px;top:114px;width:100px">Collected</span>
    <div class="tag" style="left:184px;top:134px;width:118px;height:46px;line-height:46px;font-size:20px">10,588 $</div>
    <span class="tag-cap" style="left:790px;top:148px;width:60px">Target</span>
    <div class="tag" style="left:780px;top:168px;width:80px;height:28px;line-height:28px;font-size:13px">55,000 $</div>
    <div class="track"><i></i><i></i><i></i><i></i><i></i><i></i><i></i><i></i><i></i><i></i><i></i><i></i><i></i></div>
    <span class="rider-marker"></span>
    <a class="btn-pink" href="#">Donate Now</a>
  </section>

  <section class="journals">
    <h2 class="section-title">Recent Journals</h2>
    <article class="journal" style="left:59px">
      <div class="journal-img" role="img" aria-label="Group of riders on a highway">
        <div class="journal-date"><b>25</b><small>MAY</small><small>2016</small></div>
      </div>
      <div class="journal-meta">&#9998; 1,256</div>
      <h3>Lorem Ipsum is simply dummy tex</h3>
      <p>When an unknown printer took a galley of type and scrambled it to make a type specimen book.</p>
      <a class="btn-black" href="#">Read More</a>
    </article>
    <article class="journal" style="left:485px">
      <div class="journal-img" role="img" aria-label="Riders lined up with their motorcycles">
        <div class="journal-date"><b>25</b><small>MAY</small><small>2016</small></div>
      </div>
      <div class="journal-meta">&#9998; 1,256</div>
      <h3>Lorem Ipsum is simply dummy tex</h3>
      <p>When an unknown printer took a galley of type and scrambled it to make a type specimen book.</p>
      <a class="btn-black" href="#">Read More</a>
    </article>
  </section>

  <section class="team">
    <div class="member" style="left:145px">
      <div class="avatar" role="img" aria-label="Portrait of rider Liam Corrow"></div>
      <h3>Liam Corrow</h3>
      <p>Donec sed odio dui. Etiam porta sem malesuada magna mollis euismod. Nullam id dolor id nibh ultricies.</p>
      <a class="btn-black" href="#">Read More</a>
    </div>
    <div class="member" style="left:436px">
      <div class="avatar" role="img" aria-label="Portrait of rider Oscar Venn"></div>
      <h3>Oscar Venn</h3>
      <p>Donec sed odio dui. Etiam porta sem malesuada magna mollis euismod. Nullam id dolor id nibh ultricies.</p>
      <a class="btn-black" href="#">Read More</a>
    </div>
    <div class="member" style="left:727px">
      <div class="avatar partner">KestrelWay</div>
      <h3>KestrelWay</h3>
      <p>Donec sed odio dui. Etiam porta sem malesuada magna mollis euismod. Nullam id dolor id nibh ultricies.</p>
      <a class="btn-black" href="#">Visit</a>
    </div>
  </section>

  <section class="newsletter">
    <label>Stay updated with latest news from</label>
    <div class="field">Enter Your Email</div>
    <div class="subscribe">Subscribe</div>
  </section>

  <footer class="site-footer">
    <span class="copy">Copyright © 2016 Throttle North . All Rights Reserved.</span>
    <div class="payments">We Accept :
      <span class="card"></span><span class="card"></span><span class="card"></span><span class="card"></span>
    </div>
  </footer>

</div>
</body>
</html>
```